new cosmetics brand needs label and logo design

We need a new logo and label design for a new company based in uk called Velta brooks. We need a label for our first offering, pure 99% pure aloe vera gel. The packaging bottle will be transparent the contence is also clear, we would like to see a design that will complament a transparent label. We would like designs with the colour green and we would like a picture of an aloe vera leaf featured.

```html
<!DOCTYPE html>
<html lang="en">
<head>
<meta charset="utf-8">
<title>Velta brooks – Aloe Vera Refreshing Gel Label</title>
<link href="https://fonts.googleapis.com/css2?family=Playfair+Display:wght@400&family=Dancing+Script:wght@700&family=Montserrat:wght@400;500;700&family=Poppins:wght@600;700&family=Roboto+Condensed:wght@400;700&display=swap" rel="stylesheet">
<style>
  :root {
    --green: #00a04e;
    --green-mid: #33b679;
    --green-pale: #aedbc0;
    --leaf-dark: #2f7a2a;
    --leaf-light: #8cc152;
    --ink: #111111;
    --white: #ffffff;
  }
  * { margin: 0; padding: 0; box-sizing: border-box; }
  html, body { width: 1200px; height: 1190px; overflow: hidden; background: var(--white); }
  .label { position: relative; width: 1200px; height: 1190px; overflow: hidden; background: var(--white); color: var(--ink); }
  .backdrop { position: absolute; inset: 0; width: 1200px; height: 1190px; }
  .abs { position: absolute; }

  .brand-name { font-family: "Poppins", sans-serif; font-weight: 600; color: var(--green); white-space: nowrap; }
  .brand-front { left: 145px; top: 178px; width: 285px; text-align: center; font-size: 42px; }
  .brand-back { right: 100px; top: 122px; font-size: 34px; text-align: right; }

  .purity { left: 140px; top: 362px; width: 320px; text-align: center; font-family: "Dancing Script", cursive; font-size: 36px; color: var(--green); }
  .title-front { left: 110px; top: 412px; width: 380px; text-align: center; font-family: "Playfair Display", serif; font-weight: 400; font-size: 78px; line-height: 1; }
  .gel-badge { left: 171px; top: 496px; width: 258px; height: 50px; background: var(--green); color: var(--white); font-family: "Poppins", sans-serif; font-weight: 700; font-size: 25px; line-height: 50px; text-align: center; letter-spacing: 0.5px; }
  .source { left: 120px; top: 556px; width: 360px; text-align: center; font-family: "Montserrat", sans-serif; }
  .source .line-1 { font-size: 18px; }
  .source .line-1 b { font-weight: 700; }
  .source .line-2 { font-size: 25px; font-weight: 700; margin-top: 2px; }

  .benefit { left: 155px; top: 704px; font-family: "Montserrat", sans-serif; font-weight: 500; font-size: 24px; line-height: 30px; color: var(--green); display: flex; gap: 10px; }
  .benefit svg { flex: none; margin-top: 3px; }

  .plant-art { left: 36px; top: 780px; width: 340px; height: 260px; border-radius: 50% 50% 10% 10% / 70% 70% 10% 10%; background: radial-gradient(ellipse at 50% 90%, var(--leaf-light), var(--leaf-dark) 75%, rgba(47,122,42,0) 76%); }

  .volume-front { left: 410px; top: 1106px; font-family: "Montserrat", sans-serif; color: var(--white); font-weight: 700; font-size: 45px; }
  .volume-front span { font-size: 28px; font-weight: 500; }

  .title-back { left: 702px; top: 204px; font-family: "Playfair Display", serif; font-weight: 400; font-size: 48px; line-height: 1; }
  .title-rule { left: 702px; top: 256px; width: 216px; height: 2px; background: var(--green); }
  .subtitle-back { left: 702px; top: 264px; font-family: "Poppins", sans-serif; font-weight: 600; font-size: 19px; color: var(--green); letter-spacing: 0.3px; }

  .details { left: 702px; top: 308px; width: 397px; font-family: "Roboto Condensed", sans-serif; font-size: 16px; line-height: 20px; }
  .details p { text-align: justify; }
  .details .plain { text-align: left; }
  .details h3 { font-size: 17px; font-weight: 700; color: var(--green); margin-top: 10px; }

  .batch { left: 945px; top: 606px; font-family: "Roboto Condensed", sans-serif; font-size: 16px; line-height: 27px; }
  .batch small { display: block; font-size: 13px; line-height: 14px; }
  .brace { left: 1032px; top: 606px; }
  .crimp { left: 1054px; top: 622px; font-family: "Roboto Condensed", sans-serif; font-size: 16px; line-height: 21px; }

  .net-vol { left: 945px; top: 705px; width: 87px; height: 78px; border: 2px solid var(--green); font-family: "Roboto Condensed", sans-serif; text-align: center; }
  .net-vol .head { height: 24px; font-weight: 700; font-size: 18px; line-height: 23px; color: var(--green); background: var(--white); }
  .net-vol .body { height: 50px; background: var(--green); color: var(--white); padding-top: 4px; }
  .net-vol .qty { font-weight: 700; font-size: 26px; line-height: 28px; }
  .net-vol .qty span { font-weight: 400; font-size: 18px; }
  .net-vol .note { font-size: 11px; line-height: 13px; }

  .maker { left: 750px; top: 817px; font-family: "Roboto Condensed", sans-serif; }
  .maker .label-sm { font-size: 14px; }
  .maker .company { font-size: 21px; font-weight: 700; margin-top: 6px; }
  .maker .address { font-size: 15px; }
  .maker .queries { font-size: 13px; margin-top: 10px; }
  .maker .email { font-size: 16px; margin-top: 4px; }
  .maker .email b { font-weight: 700; }

  .best-before { left: 986px; top: 818px; display: flex; align-items: flex-end; gap: 6px; font-family: "Roboto Condensed", sans-serif; font-size: 16px; line-height: 18px; text-align: right; }
  .jar { width: 44px; height: 44px; position: relative; }
  .jar .lid { position: absolute; left: 4px; top: 2px; width: 38px; height: 10px; border: 1.5px solid var(--ink); border-radius: 50%; transform: rotate(-12deg); }
  .jar .pot { position: absolute; left: 2px; top: 18px; width: 40px; height: 22px; border: 1.5px solid var(--ink); border-radius: 3px; font-size: 12px; font-weight: 700; line-height: 19px; text-align: center; }
  .cert-mark { left: 988px; top: 882px; width: 44px; height: 44px; border: 2px solid var(--ink); border-radius: 8px; }
  .recycle-mark { left: 1052px; top: 888px; width: 36px; height: 36px; border: 3px solid var(--ink); border-radius: 50%; }
</style>
</head>
<body>
<main class="label">
  <svg class="backdrop" viewBox="0 0 1200 1190" role="img" aria-label="Soft green curved bands framing the top and bottom of the label">
    <defs>
      <linearGradient id="top-band" x1="0" y1="0" x2="0" y2="1">
        <stop offset="0" stop-color="var(--green)"/>
        <stop offset="1" stop-color="var(--green-pale)"/>
      </linearGradient>
      <linearGradient id="bottom-band" x1="0" y1="0" x2="0" y2="1">
        <stop offset="0" stop-color="var(--green-pale)"/>
        <stop offset="0.55" stop-color="var(--green-mid)"/>
        <stop offset="1" stop-color="var(--green)"/>
      </linearGradient>
    </defs>
    <path fill="url(#top-band)" d="M0,0 H1200 V40 C1000,50 700,90 600,195 C500,90 200,50 0,40 Z"/>
    <path fill="url(#bottom-band)" d="M0,920 C110,1010 250,1040 380,1000 C470,970 540,880 600,836 C660,880 730,970 820,1000 C950,1040 1090,1010 1200,920 V1190 H0 Z"/>
  </svg>

  <!-- Front panel -->
  <div class="abs brand-name brand-front">Velta brooks</div>
  <div class="abs purity">99% pure</div>
  <h1 class="abs title-front">Aloe Vera</h1>
  <div class="abs gel-badge">REFREHING GEL</div>
  <div class="abs source">
    <div class="line-1">Made from <b>Inner Gel of</b></div>
    <div class="line-2">The Aloe Vera Leaf</div>
  </div>
  <div class="abs benefit">
    <svg width="26" height="26" viewBox="0 0 26 26" aria-hidden="true">
      <circle cx="12" cy="13" r="10.5" fill="none" stroke="var(--green)" stroke-width="2.5"/>
      <path d="M7 13 l4 4 l11 -12" fill="none" stroke="var(--green)" stroke-width="2.8" stroke-linecap="round" stroke-linejoin="round"/>
    </svg>
    <div>Soothing, Cooling &amp;<br>Moisturizing for Skin</div>
  </div>
  <div class="abs plant-art" role="img" aria-label="Illustration of a spiky green aloe vera plant"></div>
  <div class="abs volume-front">250 <span>ml</span></div>

  <!-- Back panel -->
  <div class="abs brand-name brand-back">Velta brooks</div>
  <h2 class="abs title-back">Aloe Vera</h2>
  <div class="abs title-rule"></div>
  <div class="abs subtitle-back">REFREHING GEL</div>

  <section class="abs details">
    <p>Velta Brooks' Aloe Vera Gel is a unique formulation made from the inner gel of the Aloe Vera leaf. Soothing, cooling and moisturising for your skin, can be used on the body, face and hair. cruelty free,</p>
    <h3>Ingredients:</h3>
    <p>Barbaden leaf extract, ceratonia siliqua, citric acid, potassium sorbate, sodium benzoate.</p>
    <h3>Use Directions:</h3>
    <p>Apply to clean dry skin, wash hands before and after use.</p>
    <h3>Warning:</h3>
    <p class="plain">for external use only. Keep out of reach of children.<br>Store in a cool dry place away from sunlight.</p>
  </section>

  <div class="abs batch">
    Mfg. Date :<br>Batch No. :<br>M.R.P. :
    <small>(Incl. All Taxes)</small>
  </div>
  <svg class="abs brace" width="14" height="76" viewBox="0 0 14 76" aria-hidden="true">
    <path d="M2 2 Q7 2 7 8 V32 Q7 38 12 38 Q7 38 7 44 V68 Q7 74 2 74" fill="none" stroke="var(--ink)" stroke-width="1.3"/>
  </svg>
  <div class="abs crimp">See on<br>Crimp</div>

  <div class="abs net-vol">
    <div class="head">Net Vol.</div>
    <div class="body">
      <div class="qty">250<span>ml</span></div>
      <div class="note">(when packed)</div>
    </div>
  </div>

  <div class="abs maker">
    <div class="label-sm">Manufactured by :</div>
    <div class="company">Company Name</div>
    <div class="address">Address line will be here.</div>
    <div class="queries">For Queries/Feedback</div>
    <div class="email">E-mail : <b>info@veltabrooks.com</b></div>
  </div>

  <div class="abs best-before">
    <div>Best<br>Before</div>
    <div class="jar"><div class="lid"></div><div class="pot">24M</div></div>
  </div>
  <div class="abs cert-mark" role="img" aria-label="Cruelty-free certification badge"></div>
  <div class="abs recycle-mark" role="img" aria-label="Recycling mark"></div>
</main>
</body>
</html>
```